Hydroponic Farm Needs a Business Card

We need a business card design for a hydroponic farm located on the Gulf Coast called 'Mossbrook Farms'. We grow many forms of lettuce and tomatoes along with other herbs and spices. We currently sell to farmer's markets though will soon be expanding to commercial accounts such as restaurants and grocery stores. The colors should be bright and vibrant to reflect the nature of our produce. The final design should communicate a professional, clean, yet friendly impression and able to be used both with farmer's markets and commercial accounts.

The pictures are an example of our product. The pictures do not have to be incorporated into the business card design.

Please put areas for information such as Names, Phone Number, E-mail address, and additional information.

Farm

```html
<!DOCTYPE html>
<html lang="en">
<head>
<meta charset="utf-8">
<title>Mossbrook Farms — Business Card</title>
<link href="https://fonts.googleapis.com/css2?family=Montserrat:wght@400;600;700&display=swap" rel="stylesheet">
<style>
  :root {
    --page: #ecebe6;
    --ink: #0d0d0d;
    --leaf: #5f9c66;
    --green: #5db443;
    --lime: #a6d13a;
    --white: #ffffff;
  }
  * { margin: 0; padding: 0; box-sizing: border-box; }
  html, body { width: 1200px; height: 1000px; overflow: hidden; }
  body {
    background: var(--page);
    font-family: 'Montserrat', sans-serif;
    position: relative;
  }
  .card {
    position: absolute;
    left: 220px;
    width: 760px;
    height: 420px;
    border-radius: 34px;
    overflow: hidden;
    background: var(--green);
    box-shadow: 0 10px 30px rgba(0,0,0,0.18);
  }
  .card--front { top: 50px; }
  .card--back { top: 530px; }

  .foliage {
    position: absolute;
    left: 0; top: 0; width: 100%;
    background:
      radial-gradient(ellipse at 50% 55%, var(--ink) 0%, #1a2a1c 28%, var(--leaf) 75%, #6aa870 100%);
  }
  .card--front .foliage { height: 322px; }
  .card--back .foliage { height: 170px; }

  .stripe {
    position: absolute;
    left: 0; width: 100%;
    height: 10px;
    background: var(--lime);
  }
  .card--front .stripe--top { top: 322px; }
  .card--front .stripe--bottom { bottom: 0; height: 12px; }
  .card--back .stripe--top { top: 170px; }

  /* Front */
  .brand {
    position: absolute;
    left: 150px; top: 110px;
    display: flex; align-items: center; gap: 22px;
  }
  .brand__dot {
    width: 128px; height: 128px;
    border-radius: 50%;
    border: 10px solid var(--green);
    background: var(--ink);
  }
  .brand__name {
    color: var(--white);
    font-weight: 700;
    font-size: 48px;
    letter-spacing: -0.5px;
  }
  .website {
    position: absolute;
    left: 0; width: 100%;
    top: 346px;
    text-align: center;
    color: var(--white);
    font-size: 27px;
    letter-spacing: 0.5px;
  }

  /* Back */
  .back-title {
    position: absolute;
    left: 0; width: 100%;
    top: 100px;
    text-align: center;
    color: var(--white);
    font-weight: 700;
    font-size: 36px;
    letter-spacing: 0.5px;
  }
  .person {
    position: absolute;
    left: 52px; top: 205px;
    color: var(--white);
  }
  .person__name { font-weight: 700; font-size: 28px; }
  .person__title { font-size: 24px; margin-top: 2px; }
  .contacts {
    position: absolute;
    left: 46px; top: 318px;
    color: var(--white);
    font-size: 21px;
    list-style: none;
  }
  .contacts li { display: flex; align-items: center; gap: 8px; margin-bottom: 12px; }
  .contacts svg { width: 22px; height: 22px; }
  .address {
    position: absolute;
    right: 56px; top: 320px;
    text-align: right;
    color: var(--white);
    font-size: 21px;
    font-style: normal;
    line-height: 1.3;
  }
  .address__label { font-weight: 700; font-size: 25px; }
</style>
</head>
<body>

<section class="card card--front">
  <div class="foliage" role="img" aria-label="Decorative leafy canopy pattern in green on black"></div>
  <div class="stripe stripe--top"></div>
  <div class="brand">
    <span class="brand__dot"></span>
    <span class="brand__name">Mossbrook Farms</span>
  </div>
  <p class="website">www.mossbrookfarms.com</p>
  <div class="stripe stripe--bottom"></div>
</section>

<section class="card card--back">
  <div class="foliage" role="img" aria-label="Decorative leafy canopy pattern in green on black"></div>
  <h1 class="back-title">MOSSBROOK FARMS</h1>
  <div class="stripe stripe--top"></div>

  <div class="person">
    <p class="person__name">Name</p>
    <p class="person__title">title</p>
  </div>

  <ul class="contacts">
    <li>
      <svg viewBox="0 0 24 24" fill="none" stroke="#fff" stroke-width="2"><rect x="7" y="2" width="10" height="20" rx="2"/><line x1="11" y1="18" x2="13" y2="18"/></svg>
      (251) 555-0148
    </li>
    <li>
      <svg viewBox="0 0 24 24" fill="none" stroke="#fff" stroke-width="2"><rect x="2" y="5" width="20" height="14" rx="1"/><polyline points="2,5 12,13 22,5"/></svg>
      name@mossbrookfarms.com
    </li>
  </ul>

  <address class="address">
    <span class="address__label">Address</span><br>
    #413 dummytxt<br>
    Dummytxt dummytxt
  </address>
</section>

</body>
</html>
```